Bussiness card/stationary for healthcare consulting company
Keltova Healthcare Solutions
Use same font as used in my logo
Franklin Gothic Demi Cond
Professional
Daniel Prescott
CEO
5183 NE Bellcourt Lane
Topeka, KS 66609-2871
785-461-xxxx
dprescott@keltova.org
keltova.org
Please have the name, title, address, phone, etc. be fields that can be editted for updates and others needing business cards. I would like to be able to edit everything on the card except the logo and design. I need business cards, stationary and envelopes.

```html
<!DOCTYPE html>
<html lang="en">
<head>
<meta charset="utf-8">
<title>Keltova Healthcare Solutions – Stationery</title>
<link href="https://fonts.googleapis.com/css2?family=Libre+Franklin:wght@400;600;700&display=swap" rel="stylesheet">
<style>
  :root{
    --teal:#1d6b69;
    --teal-dark:#14504f;
    --teal-faint:#e4eeee;
    --paper:#ffffff;
    --ink:#3d4a4a;
    --muted:#7d8a8a;
    --bg:#e6e9e9;
  }
  *{box-sizing:border-box;margin:0;padding:0}
  html,body{width:1200px;height:961px;overflow:hidden}
  body{background:var(--bg);font-family:"Libre Franklin",Arial,sans-serif;color:var(--ink);position:relative}
  .piece{position:absolute;box-shadow:0 2px 10px rgba(0,0,0,.12)}
  .brand{display:flex;align-items:center;gap:10px;font-weight:700;letter-spacing:.06em;text-transform:uppercase}
  .brand-dot{border-radius:50%;flex:none}

  /* Folder */
  .folder{left:60px;top:60px;width:400px;height:520px;background:var(--teal);display:flex;align-items:center;justify-content:center}
  .folder .brand{color:var(--paper);font-size:38px}
  .folder .brand-dot{width:34px;height:34px;background:var(--paper)}

  /* Letterhead */
  .letterhead{left:500px;top:60px;width:400px;height:520px;background:var(--paper);overflow:hidden}
  .letterhead .brand{position:absolute;left:28px;top:26px;color:var(--teal);font-size:20px}
  .letterhead .brand-dot{width:18px;height:18px;background:var(--teal)}
  .letterhead .contact{position:absolute;right:26px;top:24px;font-size:7.5px;line-height:1.6;text-align:right;color:var(--muted)}
  .letterhead .watermark{position:absolute;left:110px;top:170px;width:180px;height:180px;border-radius:50%;background:var(--teal-faint)}
  .letterhead .footer-rule{position:absolute;left:28px;right:28px;bottom:26px;height:3px;background:var(--teal)}

  /* Business card front */
  .card{width:240px;height:137px;background:var(--paper)}
  .card-front{left:930px;top:60px;padding:18px 18px}
  .card-front .brand{color:var(--teal);font-size:18px}
  .card-front .brand-dot{width:16px;height:16px;background:var(--teal)}
  .card-front .person{margin-top:16px}
  .card-front .name{font-size:12px;font-weight:700;color:var(--teal)}
  .card-front .title{font-size:8px;color:var(--muted);margin-top:2px}
  .card-front .details{position:absolute;right:18px;bottom:14px;font-size:7px;line-height:1.55;text-align:right}
  .card-front .tagline{position:absolute;left:18px;bottom:14px;font-size:6.5px;color:var(--muted);max-width:90px;line-height:1.4}

  /* Business card back */
  .card-back{left:930px;top:230px;background:var(--teal);display:flex;align-items:center;justify-content:center}
  .card-back .brand{color:var(--paper);font-size:22px}
  .card-back .brand-dot{width:20px;height:20px;background:var(--paper)}

  /* Envelope */
  .envelope{left:60px;top:650px;width:560px;height:243px;background:var(--paper)}
  .envelope .brand{position:absolute;left:26px;top:22px;color:var(--teal);font-size:20px}
  .envelope .brand-dot{width:18px;height:18px;background:var(--teal)}
  .envelope .return{position:absolute;left:26px;top:54px;font-size:8px;color:var(--muted);line-height:1.5}
  .envelope .band{position:absolute;left:0;right:0;bottom:0;height:8px;background:var(--teal)}

  /* Disc */
  .disc{left:680px;top:640px;width:260px;height:260px;border-radius:50%;background:var(--paper);display:flex;align-items:center;justify-content:center}
  .disc .hub{position:absolute;left:105px;top:105px;width:50px;height:50px;border-radius:50%;background:var(--bg);box-shadow:inset 0 0 0 8px #d6dcdc}
  .disc .brand{position:absolute;top:70px;color:var(--teal);font-size:17px}
  .disc .brand-dot{width:14px;height:14px;background:var(--teal)}
  .disc .web{position:absolute;bottom:62px;font-size:8px;color:var(--muted)}
</style>
</head>
<body>

  <section class="piece folder" aria-label="Presentation folder cover">
    <div class="brand"><span class="brand-dot"></span>Keltova</div>
  </section>

  <section class="piece letterhead" aria-label="Letterhead">
    <div class="brand"><span class="brand-dot"></span>Keltova</div>
    <address class="contact">
      5183 NE Bellcourt Lane<br>
      Topeka, KS 66609-2871<br>
      785-461-xxxx<br>
      keltova.org
    </address>
    <div class="watermark"></div>
    <div class="footer-rule"></div>
  </section>

  <section class="piece card card-front" aria-label="Business card front">
    <div class="brand"><span class="brand-dot"></span>Keltova</div>
    <div class="person">
      <div class="name">Daniel Prescott</div>
      <div class="title">CEO</div>
    </div>
    <div class="tagline">Keltova Healthcare Solutions</div>
    <address class="details">
      5183 NE Bellcourt Lane<br>
      Topeka, KS 66609-2871<br>
      785-461-xxxx<br>
      dprescott@keltova.org<br>
      keltova.org
    </address>
  </section>

  <section class="piece card card-back" aria-label="Business card back">
    <div class="brand"><span class="brand-dot"></span>Keltova</div>
  </section>

  <section class="piece envelope" aria-label="Envelope">
    <div class="brand"><span class="brand-dot"></span>Keltova</div>
    <address class="return">5183 NE Bellcourt Lane, Topeka, KS 66609-2871</address>
    <div class="band"></div>
  </section>

  <section class="piece disc" aria-label="Disc label">
    <div class="brand"><span class="brand-dot"></span>Keltova</div>
    <div class="hub"></div>
    <div class="web">keltova.org</div>
  </section>

</body>
</html>
```